Kelmora Legal Business Card

I require a corporate business card for a new legal services business.

I do not have a logo, nor do I want one.

I require a clean, neat a professional card for a law firm.

Details:

Business Name: Kelmora Legal
Name: Debra Lindqvist
Title: Corporate Services Manager
Location: Office 14 (Top Floor), Toravel Business Centre, Quinlan Grove Street, Alotau CBD, Milne Bay Province.
Postal Address: PO Box 593, Alotau, 211, Milne Bay Province, Papua New Guinea.
Contact: T: +675 6418250, F: +675 6413362, M: +675 72915867, E: dlindqvist@kelmoraexample.com.pg.

I look forward to your design submissions.

Industry/Entity Type

Legal

```html
<!DOCTYPE html>
<html lang="en">
<head>
<meta charset="utf-8">
<title>Kelmora Legal – Business Card</title>
<link rel="stylesheet" href="https://fonts.googleapis.com/css2?family=Oswald:wght@400&family=Roboto+Condensed:wght@300;400&display=swap">
<style>
  :root {
    --backdrop: #e4e4e8;
    --card-stock: #deddc8;
    --panel: #4a4a45;
    --panel-text: #f4f3ea;
    --ink: #3c3c38;
    --card-shadow: rgba(40, 40, 50, 0.18);
  }
  * { margin: 0; padding: 0; box-sizing: border-box; }
  html, body {
    width: 1200px;
    height: 900px;
    overflow: hidden;
    background: var(--backdrop);
  }
  .business-card {
    position: absolute;
    left: 100px;
    top: 170px;
    width: 1000px;
    height: 560px;
    background: var(--card-stock);
    box-shadow: 0 10px 30px var(--card-shadow);
  }
  .identity-panel {
    position: absolute;
    left: 0;
    top: 84px;
    width: 480px;
    height: 392px;
    background: var(--panel);
    border-radius: 0 26px 26px 0;
    color: var(--panel-text);
    text-align: center;
  }
  .brand-mark {
    position: absolute;
    left: 50%;
    top: 62px;
    transform: translateX(-50%);
  }
  .brand-name {
    position: absolute;
    left: 0;
    right: 0;
    top: 150px;
    font-family: "Oswald", sans-serif;
    font-weight: 400;
    font-size: 34px;
    letter-spacing: 0.5px;
  }
  .person-name {
    position: absolute;
    left: 0;
    right: 0;
    top: 252px;
    font-family: "Oswald", sans-serif;
    font-weight: 400;
    font-size: 33px;
  }
  .person-title {
    position: absolute;
    left: 0;
    right: 0;
    top: 302px;
    font-family: "Roboto Condensed", sans-serif;
    font-weight: 300;
    font-size: 20px;
  }
  .contact-details {
    position: absolute;
    left: 500px;
    top: 92px;
    font-family: "Roboto Condensed", sans-serif;
    font-weight: 300;
    font-size: 21px;
    line-height: 29px;
    color: var(--ink);
    font-style: normal;
  }
  .contact-lines { list-style: none; }
  .postal-lines { margin-top: 28px; }
</style>
</head>
<body>
  <section class="business-card">
    <div class="identity-panel">
      <svg class="brand-mark" width="34" height="34" viewBox="0 0 34 34" aria-hidden="true">
        <circle cx="17" cy="17" r="15" fill="var(--panel-text)"/>
      </svg>
      <h1 class="brand-name">Kelmora Legal</h1>
      <h2 class="person-name">Debra Lindqvist</h2>
      <p class="person-title">Corporate Services Manager</p>
    </div>
    <address class="contact-details">
      <ul class="contact-lines">
        <li>T: +675 6418250</li>
        <li>F: +675 6413362</li>
        <li>M: +675 72915867</li>
        <li>E: dlindqvist@kelmoraexample.com.pg.</li>
      </ul>
      <ul class="contact-lines postal-lines">
        <li>Office 14 (Top Floor),</li>
        <li>Toravel Business Centre,</li>
        <li>Quinlan Grove Street, Alotau CBD,</li>
        <li>Milne Bay Province.</li>
        <li>PO Box 593, Alotau, 211,</li>
        <li>Milne Bay Province, Papua New Guinea.</li>
      </ul>
    </address>
  </section>
</body>
</html>
```